Redesign Of Flower Delivery Subscription Service Website

I need a revamped website of www.petal-rush.com

Please revamp current design using same content....

Target Market(s)

people who buy flowers. Brides, wedding planners, wedding photographer, married man, boyfriend, etc.

Industry/Entity Type

Florist

Number of Pages Required

5+ page

Colors

Designer to choose colors to be used in the design.

Requirements
Must have
• I need a revamped website of www.petal-rush.com
• Please revamp current design using same content....
Nice to have
Should not have

```html
<!DOCTYPE html>
<html lang="en">
<head>
<meta charset="utf-8">
<title>Petal Rush – Flower Subscription</title>
<link rel="stylesheet" href="https://fonts.googleapis.com/css2?family=Montserrat:wght@400;600;700;800&family=Open+Sans:wght@400;600;700&display=swap">
<style>
:root{
  --green:#7cc242;
  --green-dark:#5fa52c;
  --orange:#f7a11a;
  --ink:#222;
  --text:#555;
  --light:#f1efef;
  --dark:#2d2d2d;
  --white:#fff;
  --grey-icon:#6d6d6d;
}
*{box-sizing:border-box;margin:0;padding:0}
html,body{width:1200px;height:5000px;overflow:hidden}
body{position:relative;background:var(--white);font-family:"Open Sans",Arial,sans-serif;color:var(--text)}
.abs{position:absolute}
.btn{position:absolute;display:flex;align-items:center;justify-content:center;font-family:"Montserrat",sans-serif;font-weight:700;font-size:14px;text-transform:uppercase;color:var(--white);white-space:nowrap}
.btn-orange{background:var(--orange)}
.btn-green{background:var(--green)}
.btn-outline{border:2px solid var(--green);color:var(--green);background:var(--white)}
.photo{position:absolute}
h2,h3,h4{font-family:"Montserrat",sans-serif}

/* header */
.logo{position:absolute;display:flex;align-items:center;gap:10px;font-family:"Montserrat",sans-serif;font-weight:700;font-size:34px;color:var(--green-dark);white-space:nowrap}
.logo .dot{width:14px;height:14px;background:var(--green);border-radius:50%}
.logo-sub{position:absolute;font-size:11px;color:var(--green-dark)}
.nav{position:absolute;left:140px;top:110px;display:flex;gap:30px;font-family:"Montserrat",sans-serif;font-weight:600;font-size:13px;color:var(--ink);text-transform:uppercase;white-space:nowrap}
.nav .active{color:var(--green);border-bottom:2px solid var(--green);padding-bottom:4px}
.follow{position:absolute;left:870px;top:30px;font-size:11px;font-weight:700;color:var(--ink)}
.social{position:absolute;top:50px;width:24px;height:24px;border-radius:4px;background:var(--grey-icon)}

/* hero */
.hero-box{position:absolute;left:725px;top:285px;width:390px;height:275px;background:rgba(30,30,30,.82);border-radius:6px;padding:34px 40px;color:var(--white)}
.hero-box h2{font-size:32px;font-weight:800;white-space:nowrap}
.hero-box p{font-size:20px;line-height:1.3;margin-top:6px}
.hero-box .price{color:var(--green);font-weight:700}
.dots{position:absolute;left:560px;top:647px;display:flex;gap:14px}
.dots span{width:9px;height:9px;border-radius:50%;background:#ddd}
.dots span:first-child{background:var(--white)}

/* features */
.feature{position:absolute;top:770px;width:298px;height:245px;border:1px solid #e3e3e3;border-bottom:3px solid var(--green);text-align:center;padding-top:84px}
.feature .icon{position:absolute;left:118px;top:-28px;width:62px;height:62px;border-radius:50%;background:var(--green);display:flex;align-items:center;justify-content:center}
.feature h3{font-size:17px;font-weight:600;color:var(--ink)}
.feature p{font-size:12px;line-height:1.5;margin:10px 22px 0}
.feature .btn{left:99px;top:188px;width:100px;height:30px;font-size:12px}

/* subscribe */
.subscribe{position:absolute;left:0;top:1080px;width:1200px;height:440px;background:var(--light)}
.subscribe h2{position:absolute;left:180px;top:95px;font-size:30px;font-weight:700;color:var(--ink)}
.subscribe h4{position:absolute;left:180px;top:140px;font-size:15px;font-weight:600;color:var(--ink);letter-spacing:1px}
.subscribe p{position:absolute;left:145px;top:180px;width:230px;font-size:12px;line-height:1.5;text-align:center}
.plan-label{position:absolute;background:var(--white);padding:8px 14px;font-family:"Montserrat",sans-serif;font-weight:700;font-size:14px;color:var(--ink)}

/* set it */
.frame{position:absolute;border:2px solid var(--green)}
.tag{position:absolute;border:2px solid var(--green);background:var(--white);color:var(--green);font-family:"Montserrat",sans-serif;font-weight:700;font-size:15px;display:flex;align-items:center;justify-content:center;text-transform:uppercase;text-align:center}
.copy{position:absolute;font-size:12px;line-height:1.55}

/* green band */
.band{position:absolute;left:0;top:2265px;width:1200px;height:525px;background:var(--green)}
.band h2{position:absolute;left:495px;top:60px;font-size:30px;font-weight:700;color:var(--white);white-space:nowrap}
.band p{position:absolute;left:495px;top:105px;width:520px;font-size:21px;line-height:1.35;color:var(--white)}

/* promos */
.promo-title{position:absolute;font-family:"Montserrat",sans-serif;font-weight:800;color:var(--white);text-transform:uppercase;line-height:1.2}

.section-title{position:absolute;left:0;width:1200px;text-align:center;font-family:"Montserrat",sans-serif;font-weight:800;font-size:28px;color:var(--ink)}
.how-layer{z-index:2}

/* footer */
.footer{position:absolute;left:0;top:4620px;width:1200px;height:380px;background:var(--dark);color:#ccc}
.footer h4{position:absolute;top:55px;font-size:12px;font-weight:700;color:var(--white);text-transform:uppercase}
.footer .line{position:absolute;font-size:12px;display:flex;align-items:center;gap:10px}
.footer .ic{width:22px;height:22px;border-radius:50%;background:var(--grey-icon);display:inline-block}
</style>
</head>
<body>

<!-- Header -->
<header>
  <div class="logo" style="left:140px;top:28px"><span class="dot"></span>Petal Rush</div>
  <div class="logo-sub" style="left:164px;top:74px">Harbor Bloom Company</div>
  <div class="btn btn-green" style="left:555px;top:35px;width:138px;height:40px">Buy Now</div>
  <div class="btn btn-outline" style="left:710px;top:35px;width:130px;height:40px;font-size:12px;color:var(--ink);border-color:#bbb;font-weight:600">My Account</div>
  <div class="follow">FOLLOW US</div>
  <div class="social" style="left:870px"></div>
  <div class="social" style="left:900px"></div>
  <div class="social" style="left:930px"></div>
  <div class="social" style="left:960px"></div>
  <nav class="nav">
    <span class="active">Home</span><span>How It Works</span><span>Delivery Areas</span><span>Franchise</span><span>Blog</span><span>Help</span><span>Free Flowers Monthly</span><span>Corporate Arrangements</span>
  </nav>
</header>

<!-- Hero -->
<section>
  <div class="photo" role="img" aria-label="Bouquet of pink tulips wrapped in kraft paper on a wooden table" style="left:0;top:145px;width:1200px;height:545px;background:linear-gradient(120deg,#6b4a3a 0%,#8a6350 35%,#caa0a8 55%,#5a3e30 100%)"></div>
  <div class="hero-box">
    <h2>ALWAYS FRESH</h2>
    <p>Beautiful Flower Arrangements<br>Delivered Monthly <span class="price">$69.95/MTH</span><br><strong style="font-size:16px">($100 value)</strong></p>
    <div class="btn btn-green" style="left:40px;top:208px;width:130px;height:38px">Buy Now</div>
  </div>
  <div class="dots"><span></span><span></span><span></span><span></span><span></span></div>
</section>

<!-- Features -->
<section>
  <div class="feature" style="left:140px">
    <div class="icon"><svg width="28" height="32" viewBox="0 0 28 32"><path d="M6 2h16l-2 8c4 3 5 9 3 14l-3 6H8l-3-6C3 19 4 13 8 10z" fill="#fff"/></svg></div>
    <h3>Free Vase</h3>
    <p>We're sure you would agree that beautiful flowers deserve to be placed in a beautiful setting.</p>
    <div class="btn btn-orange">Read More</div>
  </div>
  <div class="feature" style="left:455px">
    <div class="icon"><svg width="34" height="24" viewBox="0 0 34 24"><rect x="1" y="3" width="20" height="14" fill="#fff"/><path d="M21 7h7l5 5v5H21z" fill="#fff"/><circle cx="8" cy="19" r="3.5" fill="#fff" stroke="#7cc242" stroke-width="2"/><circle cx="26" cy="19" r="3.5" fill="#fff" stroke="#7cc242" stroke-width="2"/></svg></div>
    <h3>Free Delivery</h3>
    <p>Why pay for flower delivery when you can receive it for free? That's right, FREE!</p>
    <div class="btn btn-orange">Read More</div>
  </div>
  <div class="feature" style="left:770px">
    <div class="icon"><svg width="30" height="30" viewBox="0 0 30 30"><path d="M15 3l8 9h-5v8h-6v-8H7z" fill="#fff"/><rect x="4" y="22" width="22" height="5" fill="#fff"/></svg></div>
    <h3>Free Upgrade</h3>
    <p>Are you a member of our monthly subscription service? Hi Petal Rush members.</p>
    <div class="btn btn-orange">Read More</div>
  </div>
</section>

<!-- Subscribe -->
<section class="subscribe">
  <h2>SUBSCRIBE</h2>
  <h4>TO PETAL RUSH</h4>
  <p>Every moment of life could be cherished perfectly…. If you choose wisely. To make your day more treasured, remember that flowers are the smartest choice when delivered through our monthly PetalRush subscription based delivery service.</p>
  <div class="btn btn-orange" style="left:178px;top:335px;width:165px;height:36px">View All Plans</div>
  <svg class="abs" style="left:968px;top:42px" width="90" height="20" viewBox="0 0 90 20"><path d="M2 10h28M2 10l7-6M2 10l7 6M60 10h28M88 10l-7-6M88 10l-7 6" stroke="#333" stroke-width="2" fill="none"/></svg>
  <div class="photo" role="img" aria-label="Pink roses in a round gift box" style="left:440px;top:95px;width:300px;height:285px;background:linear-gradient(135deg,#f3d6dd,#d9708a 60%,#f5e4e6)"></div>
  <div class="plan-label" style="left:440px;top:312px">MONTHLY PLANS</div>
  <div class="photo" role="img" aria-label="Mixed pink and white rose bouquet" style="left:755px;top:95px;width:300px;height:285px;background:linear-gradient(135deg,#e8b8c0,#c54f6c 55%,#f0d0d5)"></div>
  <div class="plan-label" style="left:755px;top:312px">WEEKLY PLANS</div>
</section>

<!-- Set it and forget it -->
<section>
  <div class="frame" style="left:118px;top:1585px;width:280px;height:285px"></div>
  <div class="photo" role="img" aria-label="Purple and white flower arrangement in a vase" style="left:126px;top:1593px;width:264px;height:269px;background:linear-gradient(160deg,#6a4a6e,#9a6aa0 50%,#d8c8d0)"></div>
  <div class="tag" style="left:145px;top:1893px;width:245px;height:44px">Set It and Forget It</div>
  <p class="copy" style="left:128px;top:1958px;width:265px">PetalRush is a "SET IT and FORGET IT" subscription based flower delivery service.<br><br>For an Amazing price PetalRush will hand deliver a gorgeous arrangement directly to anyone you want every month without you having to worry about it.</p>

  <div class="frame" style="left:462px;top:1660px;width:270px;height:285px"></div>
  <div class="photo" role="img" aria-label="Cream and pink rose bouquet in a glass vase" style="left:470px;top:1668px;width:254px;height:269px;background:linear-gradient(160deg,#f6efe6,#e4c7b5 55%,#c79a8a)"></div>
  <div class="tag" style="left:478px;top:1970px;width:250px;height:44px">Buy Never Forget Again</div>
  <p class="copy" style="left:465px;top:2035px;width:265px">When setting up your account, you can choose exact delivery dates for the months that have special days such as your Anniversary, Birthday, Valentines Day and Mothers Day. You might forget but we won't, we have got ya covered!</p>

  <div class="frame" style="left:810px;top:1745px;width:265px;height:280px"></div>
  <div class="photo" role="img" aria-label="Peach and pink rose bouquet" style="left:818px;top:1753px;width:249px;height:264px;background:linear-gradient(160deg,#f4e3dc,#e38a86 55%,#d56a6e)"></div>
  <div class="abs" style="left:990px;top:1755px;width:36px;height:30px;background:#7a4b3a"></div>
  <div class="tag" style="left:822px;top:2047px;width:240px;height:58px;font-size:14px">Making Someone's<br>Day Better</div>
  <p class="copy" style="left:818px;top:2123px;width:255px">Be the hero in that special someone's life each and every month.It feels good to make a difference in your loved ones day.</p>
</section>

<!-- Weekly deliveries -->
<section class="band">
  <div class="photo" role="img" aria-label="Mother and daughter holding yellow tulips" style="left:145px;top:70px;width:288px;height:300px;background:linear-gradient(135deg,#f0ede8,#e5dccb 50%,#d8c28a)"></div>
  <h2>Weekly and Bi-Weekly Deliveries</h2>
  <p>Lorem Ipsum is simply dummy text of the printing and typesetting industry.</p>
  <div class="btn btn-outline" style="left:495px;top:195px;width:130px;height:36px;font-size:12px;border-color:var(--white)">Read More</div>
  <div class="abs" style="left:495px;top:290px;width:262px;height:235px;background:var(--white)"></div>
  <div class="photo" role="img" aria-label="Person holding a colourful bouquet" style="left:505px;top:300px;width:242px;height:225px;background:linear-gradient(160deg,#d9d7d2,#e2a24f 55%,#7a8aa0)"></div>
  <div class="abs" style="left:790px;top:235px;width:265px;height:280px;background:var(--white)"></div>
  <div class="photo" role="img" aria-label="Person giving a rose bouquet" style="left:800px;top:245px;width:245px;height:260px;background:linear-gradient(160deg,#e8dcd2,#c88a86 50%,#8a4a4c)"></div>
</section>

<!-- Promos -->
<section>
  <div class="photo" role="img" aria-label="Red roses in a paper cone on a coral background" style="left:143px;top:2840px;width:510px;height:335px;background:linear-gradient(120deg,#f26b78 0%,#f06374 55%,#a8283a 100%)"></div>
  <div class="promo-title" style="left:190px;top:2975px;font-size:23px">One Time<br>Bouquets Are<br>Now Available!</div>
  <div class="btn btn-orange" style="left:200px;top:3083px;width:115px;height:32px;font-size:12px">Read More</div>

  <div class="photo" role="img" aria-label="Hand holding a wildflower bouquet" style="left:143px;top:3195px;width:510px;height:325px;background:linear-gradient(120deg,#e6e6e4,#d9c68a 40%,#9b7ab0 60%,#e8e8e6)"></div>
  <div class="promo-title" style="left:425px;top:3390px;font-size:22px;color:var(--ink)">Refer a Friend</div>
  <div class="abs" style="left:425px;top:3420px;font-size:18px;color:var(--ink)">and get a Free BouQuet</div>
  <div class="btn btn-orange" style="left:425px;top:3450px;width:150px;height:32px;font-size:12px">Refer a Friend</div>

  <div class="photo" role="img" aria-label="Pink roses in a round hat box" style="left:683px;top:2840px;width:372px;height:680px;background:linear-gradient(180deg,#dedad7 0%,#dedad7 45%,#ef7fa6 70%,#e2dedb 100%)"></div>
  <div class="promo-title" style="left:683px;top:2887px;width:372px;text-align:center;font-size:22px;color:var(--ink)">Over 50 Couples<br>Enjoyed</div>
  <p class="abs" style="left:743px;top:2955px;width:252px;text-align:center;font-size:12px;line-height:1.5">There are many variations of passages of Lorem Ipsum available, but the majority have suffered.</p>
  <div class="btn btn-orange" style="left:813px;top:3033px;width:112px;height:32px;font-size:12px">Read More</div>
</section>

<!-- Free upgrade (drawn before the video panel so the panel sits on top) -->
<section>
  <div class="photo" role="img" aria-label="Colourful flowers framing a light wooden surface" style="left:0;top:4100px;width:1200px;height:520px;background:radial-gradient(ellipse at center,#f7f3ee 45%,#f0c8b0 75%,#d8684a 100%)"></div>
  <h2 class="section-title" style="top:4335px;font-size:27px">RECEIVE A FREE UPGRADE</h2>
  <div class="abs" style="left:325px;top:4410px;width:550px;height:50px;background:var(--white);border:1px solid #ddd"></div>
  <svg class="abs" style="left:343px;top:4428px" width="18" height="14" viewBox="0 0 18 14"><rect width="18" height="14" fill="#333"/><path d="M0 0l9 7 9-7" stroke="#fff" stroke-width="1.5" fill="none"/></svg>
  <div class="abs" style="left:372px;top:4426px;font-size:13px;color:#777">YOUR E MAIL ADDRESS</div>
  <div class="btn btn-orange" style="left:760px;top:4418px;width:105px;height:34px">Submit</div>
</section>

<!-- How it works -->
<section>
  <h2 class="section-title" style="top:3600px">HOW IT WORKS</h2>
  <div class="abs how-layer" style="left:143px;top:3683px;width:912px;height:470px;background:var(--white);box-shadow:0 2px 14px rgba(0,0,0,.15)"></div>
  <div class="logo how-layer" style="left:290px;top:3885px;font-size:40px;color:#333"><span class="dot" style="background:#333"></span>Petal Rush</div>
  <svg class="abs how-layer" style="left:568px;top:3880px" width="50" height="50" viewBox="0 0 50 50" aria-label="Play video"><circle cx="25" cy="25" r="24" fill="none" stroke="#333" stroke-width="2"/><path d="M20 15l15 10-15 10z" fill="#333"/></svg>
  <div class="photo how-layer" role="img" aria-label="Hand sketching a bouquet in a vase" style="left:650px;top:3780px;width:405px;height:360px;background:linear-gradient(160deg,#fff 20%,#efefef 60%,#d9b9a0 100%)"></div>
</section>

<!-- Footer -->
<footer class="footer">
  <div class="logo" style="left:143px;top:80px;color:var(--white)"><span class="dot"></span>Petal Rush</div>
  <div class="logo-sub" style="left:167px;top:125px;color:#ccc">Harbor Bloom Company</div>
  <h4 style="left:440px">Contact Us</h4>
  <div class="line" style="left:440px;top:90px"><svg width="10" height="14" viewBox="0 0 10 14"><path d="M5 0a5 5 0 0 1 5 5c0 4-5 9-5 9S0 9 0 5a5 5 0 0 1 5-5z" fill="#fff"/></svg><span>418 Meadowlark Lane, Cedar Bay,<br>CA 90410</span></div>
  <div class="line" style="left:440px;top:140px"><svg width="12" height="12" viewBox="0 0 12 12"><path d="M2 0l3 3-1.5 2a7 7 0 0 0 3.5 3.5L9 7l3 3-2 2C5 12 0 7 0 2z" fill="#fff"/></svg>555 014-2290</div>
  <div class="line" style="left:440px;top:175px"><svg width="12" height="9" viewBox="0 0 12 9"><rect width="12" height="9" fill="#fff"/></svg>hello@petal-rush.com</div>
  <h4 style="left:712px">More Services</h4>
  <div class="line" style="left:712px;top:90px;line-height:1.5;display:block">CORPORATE ARRANGEMENTS<br>HOTEL ARRANGEMENTS<br>EVENTS<br>WEDDINGS</div>
  <h4 style="left:935px">Connect With Us</h4>
  <div class="line" style="left:935px;top:95px"><span class="ic"></span>Social Page</div>
  <div class="line" style="left:935px;top:135px"><span class="ic"></span>Updates</div>
  <div class="line" style="left:935px;top:175px"><span class="ic"></span>Network</div>
  <div class="line" style="left:143px;top:318px;font-size:11px">Privacy Policy  Terms &amp; Conditions</div>
  <div class="line" style="left:855px;top:318px;font-size:11px">Copyright @ 2019 All Rights Reserved</div>
</footer>

</body>
</html>
```